Flyer-Design für Unternehmen mit Fokus auf 3D-Messtechnik
Zielgruppe
Deutsch:
Wir sind ein Ingenieur Dienstleistungsunternehmen mit Fokus auf 3D-Messtechnik und zerstörungsfreier Prüftechnik mit kamerabasierten Systemen. Wir entwickeln Prüfalgorithmen zur automatisierten Bauteilinspektion.
Unsere Zielgruppe sind produzierende Unternehmen die ihre Qualitätskontrolle durch optische Prüfsysteme ergänzen und/oder komplexe Bauteilmessungen bei einem Dienstleister outsourcen möchten.
Englisch:
We are an engineering service company with focus on 3D measurement and non destructive testing with camera systems. We develop inspection algorithms regarding automated quality check of components. Our target group are producing companies which want to perform there quality checks by optical inspection systems and/or want to have high precise measurements of there parts.
Aufgabenstellung
The flyer should give a good overview of the companies services. The format can be 6 pages and high side but you can also be creative if another format matches well. The different business areas are:
1. 3D-Messtechnik
2. Zerstörungsfreie Prüftechnik mit bildgebenden Systemen
3. Softwareentwicklung mit Schwerpunkt optische Qualitätskontrolle
4. Machbarkeitsstudien
5. Schulungen
A first draft of content i have uploaded in a word document, please just insert it i can edit it later.
To every of the 5 business areas suggestions of pictures can be made, also from stock pictures. I will have a look in parallel.

```html
<!DOCTYPE html>
<html lang="de">
<head>
<meta charset="utf-8">
<title>Optiform Lab – Leistungsflyer</title>
<link rel="stylesheet" href="https://fonts.googleapis.com/css2?family=Ubuntu:wght@500;700&family=Open+Sans:wght@400;600;700&display=swap">
<style>
:root{
  --navy:#1b3a6b;
  --navy-deep:#16305a;
  --ink:#3a3f47;
  --paper:#ffffff;
  --stage:#eceff3;
  --line:#d9dee6;
}
*{margin:0;padding:0;box-sizing:border-box}
html,body{width:981px;height:1200px;overflow:hidden}
body{background:var(--stage);font-family:"Open Sans",Arial,sans-serif;color:var(--ink);position:relative}
.spread{position:absolute;left:40px;width:900px;height:300px;display:flex;box-shadow:0 6px 18px rgba(20,30,50,.18)}
.spread--outside{top:40px}
.spread--inside{top:375px}
.panel{position:relative;width:300px;height:300px;background:var(--paper);overflow:hidden;display:flex;flex-direction:column}
.single{position:absolute;top:720px;box-shadow:0 6px 18px rgba(20,30,50,.18)}
.single--cover{left:165px}
.single--training{left:515px}
.heading{font-family:"Ubuntu",Arial,sans-serif;font-weight:700;color:var(--navy);text-transform:uppercase;font-size:20px;line-height:1.05;letter-spacing:.3px}
.copy{font-size:7.4px;line-height:1.38;margin-top:9px}
.text-block{padding:22px 22px 14px}
.photo{flex:none}
.photo--code{height:148px;background:linear-gradient(120deg,#0b1c3a 0%,#14427a 55%,#3aa3d4 100%)}
.photo--meeting{height:150px;background:linear-gradient(110deg,#6d7480 0%,#b9c3d0 45%,#dfe6ee 70%,#8d96a3 100%)}
.photo--blur{height:190px;background:radial-gradient(circle at 30% 40%,#c79a6a 0%,#7a6a5a 35%,#3d4450 75%,#2a3240 100%)}
.photo--machine{height:150px;background:linear-gradient(135deg,#2d4f8a 0%,#8fa8d0 45%,#dfe6f2 65%,#4a6aa6 100%)}
.photo--lenses{height:150px;margin-top:auto;background:linear-gradient(90deg,#2b2e33 0%,#8a8f96 40%,#eef0f2 60%,#5e636a 100%)}
.info-bar{margin-top:auto;background:var(--navy);color:#fff;text-align:center;font-weight:700;font-size:8.6px;padding:12px 0}
.cover-brand{position:absolute;top:60px;left:0;width:100%;display:flex;flex-direction:column;align-items:center;gap:10px}
.cover-brand__mark{width:42px;height:42px;border-radius:8px;background:rgba(255,255,255,.9)}
.cover-brand__name{font-family:"Ubuntu",Arial,sans-serif;font-weight:500;color:#fff;font-size:25px;letter-spacing:1.5px;text-transform:uppercase}
.cover-band{flex:1;background:var(--navy);border-top:4px solid #fff;color:#fff;padding:20px 22px}
.cover-band__title{font-family:"Ubuntu",Arial,sans-serif;font-weight:700;font-size:13px;text-transform:uppercase;letter-spacing:.3px}
.cover-band__copy{font-size:8px;line-height:1.35;margin-top:8px}
.express{flex:1;background:linear-gradient(160deg,#2a4a80 0%,var(--navy-deep) 100%);position:relative;color:#fff}
.express__frame{position:absolute;left:48px;right:48px;top:28px;bottom:24px;border:1px solid rgba(255,255,255,.75);text-align:center;padding:40px 14px 0}
.express__icon{position:absolute;left:50%;top:0;transform:translate(-50%,-50%);width:50px;height:50px;border-radius:50%;background:#fff;border:2px solid var(--navy)}
.express__title{font-family:"Ubuntu",Arial,sans-serif;font-weight:500;font-size:11px;text-transform:uppercase}
.express__copy{font-size:7.4px;line-height:1.35;margin-top:6px}
</style>
</head>
<body>

<section class="spread spread--outside">
  <article class="panel">
    <div class="text-block">
      <h2 class="heading">Software-<br>Entwicklung</h2>
      <p class="copy">Wir entwickeln Software mit Fokus auf Computer Vision Applikationen. Dazu verwenden wir eine geschwindigkeitsoptimierte Bildverarbeitungsbibliothek kombiniert mit selbst entwickelten Algorithmen. Die Kameraanbindung sowie Beleuchtungsansteuerung erfolgen in der hauseigenen Software, sie erhalten also die Computer Vision Funktionalität aus einer Hand.</p>
    </div>
    <div class="photo photo--code" role="img" aria-label="Programmcode auf blauem digitalem Hintergrund"></div>
  </article>
  <article class="panel">
    <div class="photo photo--meeting" role="img" aria-label="Besprechung vor einer digitalen Präsentationstafel"></div>
    <div class="text-block">
      <h2 class="heading">Schulung und<br>Beratung</h2>
      <p class="copy">Benötigen Sie Unterstützung bei der Programmierung Ihrer Kalibrex Messmaschine unter MessPilot oder im Bereich der digitalen Bildverarbeitung? Kontaktieren Sie uns und wir besprechen die weitere Vorgehensweise um Sie optimal zu unterstützen.</p>
    </div>
    <div class="info-bar">Mehr Infos: www.optiform-lab.net</div>
  </article>
  <article class="panel">
    <div class="photo photo--blur" role="img" aria-label="Unscharfer Büroraum im Hintergrund"></div>
    <div class="cover-brand"><span class="cover-brand__mark"></span><span class="cover-brand__name">Optiform Lab</span></div>
    <div class="cover-band">
      <h3 class="cover-band__title">Ihr kompetenter Partner.</h3>
      <p class="cover-band__copy">Im Bereich 3D-Messtechnik und<br>der zerstörungsfreien Prüftechnik.</p>
    </div>
  </article>
</section>

<section class="spread spread--inside">
  <article class="panel">
    <div class="text-block">
      <h2 class="heading">Messtechnik</h2>
      <p class="copy">Wir vermessen Ihre Bauteile entsprechend Ihren Anforderungen mit modernen Messmaschinen entweder optisch, taktil oder in Kombination der beiden Verfahren. Die Messungen werden ausschließlich in einem klimatisierten Messraum vorgenommen. Der Messbericht kann in verschiedenen Formaten z.B. als Text-, CSV-, oder Exceldatei geliefert werden und ist natürlich entsprechend Ihren Anforderungen formatierbar.</p>
    </div>
    <div class="express">
      <div class="express__frame">
        <span class="express__icon"></span>
        <h3 class="express__title">Express-Service</h3>
        <p class="express__copy">Benötigen Sie schnell Ihre Messergebnisse rufen Sie uns an, wir vereinbaren umgehend einen Termin um Ihre Bauteile abzuholen.</p>
      </div>
    </div>
  </article>
  <article class="panel">
    <div class="photo photo--machine" role="img" aria-label="Optisches Messsystem mit Kamera über einem Bauteilträger"></div>
    <div class="text-block">
      <h2 class="heading">Zerstörungsfreie<br>Prüftechnik</h2>
      <p class="copy">Sind Sie an einem Inspektionssystem zur optischen Qualitätskontrolle Ihrer Bauteile interessiert? Wir entwickeln das System entsprechend Ihren Anforderungen, von einem manuellen Inspektionsarbeitsplatz bis hin zu einer automatisierten Defekterkennung. Mit Hilfe unserer umfangreichen Computer Vision Bibliothek erhalten Sie modernste Bildverarbeitungsfunktionen.</p>
    </div>
  </article>
  <article class="panel">
    <div class="text-block">
      <h2 class="heading">Machbarkeitsstudien</h2>
      <p class="copy">Haben Sie ein Automatisierungsvorhaben im Fokus aber möchten zunächst herausarbeiten welche Computer Vision Technologien am besten für das Projekt geeignet sind? Mit welchem zeitlichen Umfang und Budget zu rechnen ist? Wie prozesssicher kann eine automatische Bildauswertung für das Projekt eingeordnet werden? Gerne führen wir eine Studie für Sie durch, dafür stehen unterschiedliche Kameras, Objektive, Filter und Beleuchtungsmodule zur Verfügung.</p>
    </div>
    <div class="photo photo--lenses" role="img" aria-label="Kameraobjektive auf hellem Untergrund"></div>
  </article>
</section>

<article class="panel single single--cover">
  <div class="photo photo--blur" role="img" aria-label="Unscharfer Büroraum im Hintergrund"></div>
  <div class="cover-brand"><span class="cover-brand__mark"></span><span class="cover-brand__name">Optiform Lab</span></div>
  <div class="cover-band">
    <h3 class="cover-band__title">Ihr kompetenter Partner.</h3>
    <p class="cover-band__copy">Im Bereich 3D-Messtechnik und<br>der zerstörungsfreien Prüftechnik.</p>
  </div>
</article>

<article class="panel single single--training">
  <div class="photo photo--meeting" role="img" aria-label="Besprechung vor einer digitalen Präsentationstafel"></div>
  <div class="text-block">
    <h2 class="heading">Schulung und<br>Beratung</h2>
    <p class="copy">Benötigen Sie Unterstützung bei der Programmierung Ihrer Kalibrex Messmaschine unter MessPilot oder im Bereich der digitalen Bildverarbeitung? Kontaktieren Sie uns und wir besprechen die weitere Vorgehensweise um Sie optimal zu unterstützen.</p>
  </div>
  <div class="info-bar">Mehr Infos: www.optiform-lab.net</div>
</article>

</body>
</html>
```